Quiet Ledger needs a book cover

Enabling people to find a new way of looking at money. If peoples thoughts, attitude and emotions around money are not inline with their goals and dreams then it is often harder to achieve their version of success.

Recognition that we have an emotional and a practical way with money.

Quiet Ledger enables people to find a sustainable (balanced) way with money for their life right now and their future.

Developing this over the years and seeing clients achieve a clear picture/idea/thought connection that is positive around money and it's purpose to them in their lives has truly been fabulous as they have then gone on to achieve their goals and dreams.

Title of book = Quiet Ledger
Tag line = Being healthy being wealthy
Authors Name = Ruth Pell
Book Size = 135 width x 185 height
Thumbnail = Cover must work well as well as full size
Looking for simple and clear app-able / icon type image
Feel free to have fun with it
A simple yet refreshing balanced, eye-catching design.

The back will include authors photo, blurb, testimonials, barcode, ISBN number & price. I will provide once front cover is sorted.

Reason: Realised that the tag line for the book was incorrect.

Target Market(s)

Individuals

Industry/Entity Type

Work

Requirements
Must have
• First work on front cover, once approved we can then do spine and back cover

```html
<!DOCTYPE html>
<html lang="en">
<head>
<meta charset="utf-8">
<title>Quiet Ledger — Book Cover</title>
<link rel="stylesheet" href="https://fonts.googleapis.com/css2?family=Arimo:wght@700&family=Reenie+Beanie&display=swap">
<style>
  :root {
    --page: #ffffff;
    --cover-cyan: #00f0f0;
    --board-green: #4ecb00;
    --tile-tan: #c99866;
    --ink: #1a1a1a;
  }
  html, body {
    margin: 0;
    padding: 0;
    width: 1200px;
    height: 1000px;
    overflow: hidden;
    background: var(--page);
  }
  .canvas {
    position: relative;
    width: 1200px;
    height: 1000px;
    background: var(--page);
  }
  .cover {
    position: absolute;
    left: 236px;
    top: 0;
    width: 731px;
    height: 1000px;
    background: var(--cover-cyan);
    overflow: hidden;
  }
  .board {
    position: absolute;
    inset: 0;
  }
  .tile-row {
    position: absolute;
    height: 88px;
    background: var(--tile-tan);
    border-radius: 4px;
  }
  .tile-row--top { left: 130px; top: 240px; width: 485px; }
  .tile-row--bottom { left: 65px; top: 364px; width: 582px; }
  .title {
    margin: 0;
    position: absolute;
    inset: 0;
    font-family: "Arimo", Arial, sans-serif;
    font-weight: 700;
    font-size: 46px;
    color: var(--ink);
  }
  .title-line {
    position: absolute;
    display: flex;
    height: 88px;
    align-items: center;
  }
  .title-line--top { left: 130px; top: 240px; }
  .title-line--bottom { left: 65px; top: 364px; }
  .title-line span {
    width: 97px;
    text-align: center;
    line-height: 1;
  }
  .tagline {
    position: absolute;
    left: 0;
    right: 0;
    top: 518px;
    margin: 0;
    text-align: center;
    font-family: "Reenie Beanie", cursive;
    font-weight: 400;
    font-size: 52px;
    color: var(--ink);
  }
  .author {
    position: absolute;
    left: 0;
    right: 0;
    top: 928px;
    margin: 0;
    text-align: center;
    font-family: "Reenie Beanie", cursive;
    font-size: 52px;
    color: var(--ink);
    padding-right: 40px;
  }
</style>
</head>
<body>
<div class="canvas">
  <div class="cover">
    <svg class="board" width="731" height="1000" viewBox="236 0 731 1000" aria-hidden="true">
      <defs>
        <filter id="board-shadow" x="-10%" y="-10%" width="120%" height="120%">
          <feDropShadow dx="-4" dy="5" stdDeviation="3" flood-color="#000" flood-opacity="0.6"/>
        </filter>
      </defs>
      <polygon class="board-card" points="103,263 895,10 1084,603 293,855"
               fill="var(--board-green)" filter="url(#board-shadow)"/>
    </svg>

    <div class="tile-row tile-row--top" role="img" aria-label="Row of wooden letter tiles"></div>
    <div class="tile-row tile-row--bottom" role="img" aria-label="Row of wooden letter tiles"></div>

    <h1 class="title" aria-label="Quiet Ledger">
      <span class="title-line title-line--top"><span>Q</span><span>U</span><span>I</span><span>E</span><span>T</span></span>
      <span class="title-line title-line--bottom"><span>L</span><span>E</span><span>D</span><span>G</span><span>E</span><span>R</span></span>
    </h1>

    <p class="tagline">Being healthy being wealthy</p>
    <p class="author">by Ruth Pell</p>
  </div>
</div>
</body>
</html>
```